Bref créative |
Website Design for Real Estate Investment Firm | ||
Brindle Oak Holding Associates | ||
Real Estate | ||
www.BrindleOakHoldingAssociates.example | ||
We are a real estate investment firm focused on the acquisition of commercial incoming producing properties and the purchase of notes and debt. We do not do residential real estate, so please do not include anything that pertains to or looks like houses. | ||
We are very open to fresh creative designs. Open with the use colors, but our main logo is dark blue and gray so colors need to be complimentary to that. Open to your font ideas too. | ||
Cutting-Edge Unique/Creative Clean/Simple Professional Conservative Exciting Sophisticated Corporate Modern Elegant Progressive Traditional |
Open to Ideas | ||
Arial Verdana |
left side | ||
www.plunaxo.example | ||
www.velmorfunds.example | ||
www.drqz.example | ||
Open to design and nav placement. | ||

```html
<!DOCTYPE html>
<html lang="en">
<head>
<meta charset="utf-8">
<title>Brindle Oak Holding Associates</title>
<link href="https://fonts.googleapis.com/css2?family=Arimo:ital,wght@0,400;0,700;1,400&family=Cinzel:wght@600&display=swap" rel="stylesheet">
<style>
:root{
  --navy-deep:#081640;
  --navy:#0f2460;
  --panel:#1b2f70;
  --panel-line:#3a52a0;
  --blue-btn:#2c4ea8;
  --white:#ffffff;
  --text-dark:#1c2540;
  --text-soft:#d6def5;
  --link:#9fc0ff;
  --gray:#8a93a8;
  --cream:#efe7c6;
}
*{box-sizing:border-box;margin:0;padding:0}
html,body{width:1200px;height:901px;overflow:hidden}
body{
  position:relative;
  font-family:"Arimo",Arial,sans-serif;
  background:radial-gradient(ellipse at 50% 35%,#1c3580 0%,var(--navy) 45%,var(--navy-deep) 100%);
  color:var(--white);
}
.brand{position:absolute;left:231px;top:16px;display:flex;align-items:center;gap:10px}
.brand-mark{width:40px;height:40px;background:var(--white)}
.brand-name{font-family:"Cinzel",Georgia,serif;font-weight:600;color:var(--white);line-height:1.05;font-size:22px;letter-spacing:1px}
.brand-name span{display:block;font-size:13px;letter-spacing:2.6px}
.account{position:absolute;top:28px;left:762px;display:flex;gap:10px}
.account a{display:block;font-size:11px;padding:5px 10px;border-radius:2px;text-decoration:none;border:1px solid #c9c0a0}
.btn-login{background:var(--cream);color:var(--text-dark)}
.btn-create{background:var(--blue-btn);color:var(--white);border-color:#6d86cc !important}
.main-nav{position:absolute;left:231px;top:78px;width:743px;height:32px;background:linear-gradient(#ffffff,#e4e8f0);display:flex;align-items:center;justify-content:space-between;padding:0 18px;font-size:12px;color:var(--text-dark)}
.main-nav .sep{color:#9aa3b8}
.hero{position:absolute;left:231px;top:114px;width:743px;height:283px;background:linear-gradient(100deg,#e9edf3 0%,#c7d0de 30%,#6f8bb8 55%,#2d4f8e 75%,#a9c2e4 100%)}
.hero-caption{position:absolute;left:50px;top:182px;width:693px;height:62px;background:linear-gradient(90deg,rgba(255,255,255,0),rgba(255,255,255,.92) 12%);color:var(--navy);font-size:15px;line-height:1.4;padding:9px 0 0 45px;white-space:nowrap}
.hero-caption span{display:block}
.hero-caption span + span{margin-left:76px}
.content{position:absolute;left:231px;top:414px;width:743px;height:306px;background:var(--panel);border:1px solid var(--panel-line)}
.col-main{position:absolute;left:6px;top:8px;width:497px}
.section-title{font-size:17px;color:var(--white);font-weight:400}
.col-main p{font-size:9.5px;line-height:1.45;color:var(--text-soft);margin-top:6px}
.more{display:block;text-align:right;font-size:9.5px;color:var(--link);margin-top:2px}
.divider{height:1px;background:var(--panel-line);margin:10px 0}
.about{position:relative}
.about-text{width:325px}
.about-photo{position:absolute;left:338px;top:22px;width:156px;height:102px;background:linear-gradient(135deg,#f2f3f5,#b8c0cf)}
.about .more{position:absolute;left:338px;width:156px;top:128px}
.col-side{position:absolute;left:518px;top:14px;width:219px}
.box-head{background:linear-gradient(var(--navy),var(--navy-deep));border:1px solid var(--panel-line);font-size:14px;padding:6px 8px}
.testimonials-body{background:var(--white);color:var(--text-dark);padding:6px 10px;font-size:9px;line-height:1.35;height:126px}
.testimonials-body b{display:block;margin-top:4px;font-size:9px}
.testimonials-body .more{color:var(--blue-btn);font-size:9px}
.portfolio{margin-top:8px}
.portfolio-thumbs{display:flex;gap:8px;padding:8px 8px;background:var(--panel);align-items:center}
.thumb{width:86px;height:70px;background:linear-gradient(160deg,#d8d1bf,#5c4a36)}
.arrow{width:0;height:0;border-top:6px solid transparent;border-bottom:6px solid transparent}
.arrow.left{border-right:7px solid var(--text-soft)}
.arrow.right{border-left:7px solid var(--text-soft)}
.investors{position:absolute;left:231px;top:725px;width:743px;height:132px;background:var(--white)}
.investors-tab{position:absolute;left:6px;top:8px;background:linear-gradient(var(--navy),var(--navy-deep));font-size:13px;padding:6px 12px;border-radius:2px}
.investor-row{position:absolute;top:42px;left:20px;right:20px;display:flex;justify-content:space-around}
.investor{text-align:center;color:var(--blue-btn);font-size:11px;font-weight:700}
.investor-avatar{width:58px;height:62px;margin:0 auto 6px;background:linear-gradient(#b5bcc8,#6b7485);border-radius:4px}
.footer{position:absolute;left:231px;top:862px;width:743px;height:26px;display:flex;align-items:center;justify-content:space-between;font-size:9px;color:var(--text-soft)}
.follow{display:flex;align-items:center;gap:5px}
.follow i{display:block;width:14px;height:14px;background:var(--white)}
</style>
</head>
<body>
<header>
  <div class="brand">
    <div class="brand-mark"></div>
    <div class="brand-name">BRINDLE OAK<span>HOLDING ASSOCIATES</span></div>
  </div>
  <div class="account">
    <a class="btn-login" href="#">Member Login</a>
    <a class="btn-create" href="#">Create Account</a>
  </div>
  <nav class="main-nav">
    <span>Home</span><span class="sep">|</span><span>About Us</span><span class="sep">|</span><span>Investment Services</span><span class="sep">|</span><span>Global Portfolio</span><span class="sep">|</span><span>News &amp; Events</span><span class="sep">|</span><span>Investors</span><span class="sep">|</span><span>Contact Us</span>
  </nav>
</header>

<section class="hero" role="img" aria-label="Photo of a hand stacking coins beside glass office towers">
  <div class="hero-caption"><span>We are focused on the acquisition of commercial</span><span>incoming producing properties and the purchase of notes and debt.</span></div>
</section>

<main class="content">
  <div class="col-main">
    <h2 class="section-title">Welcome to Brindle Oak Holding Associates!</h2>
    <p>Brindle Oak Holding Associates acquires commercial income producing properties across the region. Our team evaluates office, retail and industrial assets with care, and purchases performing and non performing notes and debt. We partner with investors who value steady returns, clear reporting and disciplined long term planning for every holding in the portfolio.</p>
    <a class="more" href="#">» Read More</a>
    <div class="divider"></div>
    <div class="about">
      <div class="about-text">
        <h2 class="section-title">About Us</h2>
        <p>Founded by seasoned investors, we focus on assets that deliver reliable income.</p>
        <p>Each acquisition is reviewed for location, tenant strength and long term value. We work closely with lenders, brokers and owners to close transactions quickly and fairly, and we manage every property with the same attention we give our own capital and our partners' trust.</p>
      </div>
      <div class="about-photo" role="img" aria-label="Photo of hands signing a contract with a pen"></div>
      <a class="more" href="#">» Read More</a>
    </div>
  </div>

  <aside class="col-side">
    <div class="testimonials">
      <h3 class="box-head">Testimonials</h3>
      <div class="testimonials-body">
        <b>11/06/2012</b>
        A clear and honest partner on every deal we closed.
        <a class="more" href="#">» Read More</a>
        <b>11/06/2012</b>
        Steady returns and timely reports every single quarter.
        <a class="more" href="#">» Read More</a>
      </div>
    </div>
    <div class="portfolio">
      <h3 class="box-head">Portfolio</h3>
      <div class="portfolio-thumbs">
        <span class="arrow left"></span>
        <div class="thumb" role="img" aria-label="Photo of a commercial building interior"></div>
        <div class="thumb" role="img" aria-label="Photo of a commercial property exterior"></div>
        <span class="arrow right"></span>
      </div>
    </div>
  </aside>
</main>

<section class="investors">
  <h3 class="investors-tab">New Investors</h3>
  <div class="investor-row">
    <div class="investor"><div class="investor-avatar" role="img" aria-label="Investor portrait placeholder"></div>Lorem ipsum</div>
    <div class="investor"><div class="investor-avatar" role="img" aria-label="Investor portrait placeholder"></div>Lorem ipsum</div>
    <div class="investor"><div class="investor-avatar" role="img" aria-label="Investor portrait placeholder"></div>Lorem ipsum</div>
    <div class="investor"><div class="investor-avatar" role="img" aria-label="Investor portrait placeholder"></div>Lorem ipsum</div>
    <div class="investor"><div class="investor-avatar" role="img" aria-label="Investor portrait placeholder"></div>Lorem ipsum</div>
    <div class="investor"><div class="investor-avatar" role="img" aria-label="Investor portrait placeholder"></div>Lorem ipsum</div>
  </div>
</section>

<footer class="footer">
  <span>Copyright © 2012 | Brindle Oak Holding Associates. All Rights Reserved. | Terms and Condition</span>
  <span class="follow">Follow Us: <i></i><i></i></span>
</footer>
</body>
</html>
```